Wine Label for a syrah wine hand crafted from walla walla valley, washington

design a wine label for the name of the brand: Orvanel. It is a wine hand crafted from Walla Walla Valley in Washington state. the label should be landscape in design, 95 mm wide by 85 mm tall. it should include the name of the brand, Orvanel, Walla Walla Valley, 2020 and Syrah. the brand is called orvanel with this in mind:

-orvanel Definition & Meaning |
1. : having (something) at the center. The solar system is helio orvanel, meaning that the sun is at its center. 2. : having (something) as a central interest, influence, subject, in the case of this wine label it is Syrah wine from Walla Walla Valley
this american vitculture area is known for wines which showcase the terrior of the area - this wine is specifically from the Rocks district where there are lots of rocks in the vineyard. think terrior, rocks, dirt, grapes that are hand crafted into a bottle of wine that will cost $125 each.

Target Market(s)

syrah lovers, Rhone valley wine lovers,

Industry/Entity Type

wine industry

Font styles to use
Sans Serif
Other font styles liked:
• freightbig in light, book and medium weights

Requirements
Must have
• the elements described in the project description, please use FreightBig font found on quillo site, light, book and medium weights
Nice to have
• a cool edgy design but elegant a the same time
Should not have
• stock pictures

```html
<!DOCTYPE html>
<html lang="en">
<head>
<meta charset="utf-8">
<title>Orvanel Syrah Label</title>
<link rel="stylesheet" href="https://fonts.googleapis.com/css2?family=Cormorant+Garamond:wght@400;500;600&display=swap">
<style>
  :root {
    --page: #ffffff;
    --label: #f5f5f5;
    --ink: #1f1712;
    --earth-dark: #3b2a1f;
    --earth-mid: #66503f;
    --earth-light: #c2b09a;
  }
  * { box-sizing: border-box; margin: 0; padding: 0; }
  html, body {
    width: 1200px;
    height: 900px;
    overflow: hidden;
    background: var(--page);
  }
  .canvas {
    position: relative;
    width: 1200px;
    height: 900px;
  }
  .label {
    position: absolute;
    left: 160px;
    top: 56px;
    width: 880px;
    height: 788px;
    background: var(--label);
    box-shadow: 2px 3px 6px rgba(0, 0, 0, 0.12);
    font-family: "Cormorant Garamond", serif;
    color: var(--ink);
  }
  .brand-name {
    position: absolute;
    top: 32px;
    left: 0;
    width: 100%;
    text-align: center;
    font-size: 60px;
    font-weight: 500;
    letter-spacing: 0.62em;
    padding-left: 0.62em;
    line-height: 1;
  }
  .emblem {
    position: absolute;
    left: 149px;
    top: 110px;
    width: 620px;
    height: 620px;
  }
  .details {
    position: absolute;
    left: 155px;
    top: 684px;
    line-height: 1;
  }
  .vintage {
    font-size: 22px;
    letter-spacing: 0.08em;
  }
  .varietal {
    margin-top: 6px;
    font-size: 29px;
    letter-spacing: 0.06em;
  }
  .region {
    margin-top: 6px;
    font-size: 15px;
    font-weight: 500;
    letter-spacing: 0.07em;
  }
</style>
</head>
<body>
<main class="canvas">
  <section class="label">
    <h1 class="brand-name">ORVANEL</h1>

    <svg class="emblem" viewBox="0 0 620 620" role="img" aria-label="Abstract emblem of concentric broken rings in earthy brown tones around an open centre, evoking rocks and terroir">
      <defs>
        <radialGradient id="earthTones" cx="50%" cy="50%" r="50%">
          <stop offset="0%" stop-color="var(--earth-dark)"/>
          <stop offset="45%" stop-color="var(--earth-mid)"/>
          <stop offset="80%" stop-color="#8a7562"/>
          <stop offset="100%" stop-color="var(--earth-light)"/>
        </radialGradient>
      </defs>
      <circle cx="310" cy="310" r="308" fill="url(#earthTones)"/>
      <circle cx="310" cy="310" r="63" fill="var(--label)"/>
    </svg>

    <div class="details">
      <p class="vintage">2020</p>
      <p class="varietal">SYRAH</p>
      <p class="region">WALLA WALLA VALLEY</p>
    </div>
  </section>
</main>
</body>
</html>
```